Oregon Pawnbroker About Us Brochure

We need to make a front/back tri-fold "about us" informative brochure using the bullet points uploaded. Our association represents licensed pawnbrokers in the state of Oregon and this will be distributed to the entire legislative body in our state. I have attached our logo, but feel free to be creative with logo to enhance the overall appearance of the brochure.

Target Market(s)

Regulators and Politicians

Industry/Entity Type

Pawnbroker

Requirements
Must have
• Professional Appearance
Nice to have
• Graphics, color scheme

```html
<!DOCTYPE html>
<html lang="en">
<head>
<meta charset="utf-8">
<title>Quick Facts About Oregon Pawnbrokers – Tri-fold Brochure</title>
<link rel="stylesheet" href="https://fonts.googleapis.com/css2?family=Oswald:wght@300;400;500&family=Open+Sans:wght@400;600;700&display=swap">
<style>
  :root{
    --orange:#e8731f;
    --orange-dark:#cf5f12;
    --ink:#4d4d4d;
    --ink-soft:#6b6b6b;
    --grey:#9b9b9b;
    --grey-mid:#bdbdbd;
    --grey-light:#e7e7e7;
    --paper:#ffffff;
    --stage:#dcdad6;
    --photo-a:#8a97a8;
    --photo-b:#c9b8a4;
  }
  *{box-sizing:border-box;margin:0;padding:0}
  html,body{width:1200px;height:2400px;overflow:hidden}
  body{background:var(--stage);font-family:"Open Sans",Arial,sans-serif;color:var(--ink);position:relative}

  .spread{position:absolute;left:40px;width:1120px;height:1080px;display:grid;grid-template-columns:repeat(3,1fr);background:var(--paper);box-shadow:0 6px 24px rgba(0,0,0,.18)}
  .spread--outside{top:80px}
  .spread--inside{top:1240px}
  .panel{position:relative;overflow:hidden;border-right:1px solid #ececec}
  .panel:last-child{border-right:0}

  .heading{font-family:"Oswald",Arial,sans-serif;font-weight:400;text-transform:uppercase;color:var(--orange);letter-spacing:.5px;line-height:1.15}
  .heading--rule::after{content:"";display:block;width:56px;height:3px;background:var(--orange);margin-top:10px}
  .body-text{font-size:14px;line-height:1.55;color:var(--ink-soft)}
  .lead{font-size:15px;font-weight:600;color:var(--ink);line-height:1.5}

  .icon-list{list-style:none;margin-top:18px}
  .icon-list li{display:flex;gap:14px;align-items:flex-start;font-size:13px;line-height:1.5;color:var(--ink-soft);margin-bottom:14px}
  .icon-list svg{flex:0 0 26px;width:26px;height:26px;margin-top:2px}

  .dot-list{list-style:none;margin-top:16px}
  .dot-list li{position:relative;padding-left:22px;font-size:13px;line-height:1.5;color:var(--ink-soft);margin-bottom:11px}
  .dot-list li::before{content:"";position:absolute;left:0;top:5px;width:10px;height:10px;border-radius:50%;background:var(--orange)}
  .sub-list{list-style:none;margin:6px 0 0 0}
  .sub-list li{padding-left:14px;margin-bottom:3px}
  .sub-list li::before{width:5px;height:5px;top:8px;background:var(--ink-soft)}

  .url-bar{position:absolute;left:0;right:0;bottom:0;height:42px;background:var(--orange);color:#fff;font-size:13px;letter-spacing:.4px;display:flex;align-items:center;justify-content:center}
  .url-bar--right{justify-content:flex-end;padding-right:26px}

  .photo{position:absolute;background:linear-gradient(135deg,var(--photo-a),var(--photo-b))}
  .photo--circle{border-radius:50%;border:8px solid var(--grey-light)}

  .assoc-mark{position:absolute;left:50%;transform:translateX(-50%);width:170px;height:170px;border-radius:50%;background:#fff;border:6px solid var(--grey-light);display:flex;align-items:center;justify-content:center;text-align:center;padding:22px}
  .assoc-mark span{font-family:"Oswald",Arial,sans-serif;font-weight:500;font-size:17px;line-height:1.2;text-transform:uppercase;color:var(--ink)}

  /* Panel: why pawnbrokers matter */
  .why{padding:46px 34px 0}
  .why .heading{font-size:25px}
  .why .body-text{margin-top:16px}
  .why .photo--circle{width:300px;height:300px;left:-70px;bottom:60px}

  /* Panel: back cover */
  .back{background:linear-gradient(180deg,#d2d2d2 0%,#efefef 45%,#f7f7f7 100%);text-align:center;padding:0 40px}
  .back .assoc-mark{top:70px}
  .back .body-text{margin-top:290px;color:var(--ink)}
  .back .rule{width:70px;height:3px;background:var(--orange);margin:28px auto}
  .back .join{font-family:"Oswald",Arial,sans-serif;font-weight:300;font-size:22px;line-height:1.35;text-transform:uppercase;color:var(--ink)}
  .back address{font-style:normal;font-size:13px;line-height:1.6;color:var(--ink-soft)}

  /* Panel: front cover */
  .cover{background:linear-gradient(180deg,#f4f4f4,#dcdcdc)}
  .cover .photo{left:0;top:0;width:100%;height:600px}
  .cover .curve{position:absolute;left:0;top:470px;width:100%;height:160px}
  .cover .assoc-mark{top:520px;width:190px;height:190px}
  .cover .title{position:absolute;right:32px;bottom:96px;text-align:right;font-family:"Oswald",Arial,sans-serif;font-weight:400;font-size:36px;line-height:1.15;text-transform:uppercase;color:var(--ink)}

  /* Panel: about our industry */
  .industry{padding:46px 32px 0}
  .industry .heading{font-size:26px}
  .industry .lead{margin-top:16px}
  .industry .photo{left:0;bottom:0;width:100%;height:250px}
  .industry .photo-arc{position:absolute;left:0;bottom:200px;width:100%;height:90px}

  /* Panel: regulation */
  .regulation{padding:46px 30px 0}
  .regulation .heading{font-size:26px;text-align:center}
  .regulation .heading--rule::after{margin:10px auto 0}
  .regulation .lead{margin-top:14px;text-align:center}
  .about-assoc{position:absolute;left:0;right:0;bottom:0;height:300px;background:linear-gradient(180deg,#a9a9a9,#8e8e8e);padding:40px 28px 0 150px;color:#fff}
  .about-assoc h3{font-family:"Oswald",Arial,sans-serif;font-weight:400;font-size:20px;line-height:1.2;text-transform:uppercase}
  .about-assoc h3::after{content:"";display:block;width:46px;height:3px;background:var(--orange);margin-top:8px}
  .about-assoc p{font-size:12.5px;line-height:1.5;margin-top:12px}
  .regulation .photo--circle{width:170px;height:170px;left:-30px;bottom:180px;border-color:#fff}

  /* Panel: statistics */
  .stats .photo{left:0;top:0;width:100%;height:280px}
  .stats .photo-arc{position:absolute;left:0;top:200px;width:100%;height:90px}
  .stats .content{position:absolute;top:310px;left:32px;right:32px}
  .stats .heading{font-size:24px}
  .stats .heading small{display:block;font-size:14px;color:var(--ink-soft);text-transform:none;margin-top:2px}
  .quick-facts{position:absolute;left:0;right:0;bottom:0;height:340px;background:linear-gradient(180deg,#b3b3b3,#959595);padding:44px 32px 0;color:#fff}
  .quick-facts h3{font-family:"Oswald",Arial,sans-serif;font-weight:400;font-size:24px;line-height:1.2;text-transform:uppercase}
  .tick-list{list-style:none;margin-top:18px}
  .tick-list li{display:flex;align-items:center;gap:12px;font-size:13.5px;font-weight:600;text-transform:uppercase;letter-spacing:.4px;margin-bottom:12px}
  .tick-list svg{width:18px;height:18px;flex:0 0 18px}
  .quick-facts .url-bar{left:auto;width:300px;bottom:30px;height:34px;border-radius:17px 0 0 17px;font-size:12px}
</style>
</head>
<body>

<svg width="0" height="0" style="position:absolute" aria-hidden="true">
  <defs>
    <symbol id="icon-ring" viewBox="0 0 26 26"><circle cx="13" cy="13" r="10.5" fill="none" stroke="#e8731f" stroke-width="2.2"/><circle cx="13" cy="13" r="4" fill="#e8731f"/></symbol>
    <symbol id="icon-tick" viewBox="0 0 18 18"><path d="M2 9.5l4.5 4.5L16 4" fill="none" stroke="#e8731f" stroke-width="3" stroke-linecap="round" stroke-linejoin="round"/></symbol>
  </defs>
</svg>

<!-- Outside spread -->
<section class="spread spread--outside">
  <article class="panel why">
    <h2 class="heading heading--rule">Why pawnbrokers are important<br>to Oregon consumers</h2>
    <p class="body-text">Without state-licensed pawnbrokers, Oregonians could be forced to borrow from unlicensed lenders with high interest and no recourse, or sell their property with no chance to get it back.</p>
    <ul class="icon-list">
      <li><svg><use href="#icon-ring"/></svg>Short, small-dollar loans such as pawn loans meet a need that banks and credit unions do not fill.</li>
      <li><svg><use href="#icon-ring"/></svg>Pawnbrokers help recover stolen property by sharing daily transaction reports with police.</li>
      <li><svg><use href="#icon-ring"/></svg>Pawnbrokers are available in rural and urban areas across the state.</li>
      <li><svg><use href="#icon-ring"/></svg>Pawnbrokers are licensed, bonded and accountable to the state of Oregon.</li>
    </ul>
    <div class="photo photo--circle" role="img" aria-label="Photo of colleagues reviewing documents together in an office"></div>
    <div class="url-bar">www.willamettepawnalliance.org</div>
  </article>

  <article class="panel back">
    <div class="assoc-mark"><span>Willamette Pawnbrokers Alliance</span></div>
    <p class="body-text">Our association members are licensed pawnbrokers who work closely with the Oregon legislature to support fair and responsible lending.</p>
    <div class="rule"></div>
    <p class="join">Not a member?<br>Interested in becoming one?<br>Join us today</p>
    <div class="rule"></div>
    <address>Willamette Pawnbrokers Alliance<br>1450 Cedar Ridge Ave, Suite 210<br>Salem, OR 97301<br>(503) 555-0142</address>
    <div class="url-bar">www.willamettepawnalliance.org</div>
  </article>

  <article class="panel cover">
    <div class="photo" role="img" aria-label="Photo of a smiling business team seated at a meeting table with charts"></div>
    <svg class="curve" viewBox="0 0 373 160" preserveAspectRatio="none" aria-hidden="true">
      <path d="M0 90 Q186 0 373 90 L373 160 L0 160 Z" fill="#f4f4f4"/>
      <path d="M0 90 Q186 0 373 90" fill="none" stroke="#ffffff" stroke-width="6"/>
    </svg>
    <div class="assoc-mark"><span>Willamette Pawnbrokers Alliance</span></div>
    <h1 class="title">Quick facts about<br>Oregon pawnbrokers</h1>
    <div class="url-bar url-bar--right">www.willamettepawnalliance.org</div>
  </article>
</section>

<!-- Inside spread -->
<section class="spread spread--inside">
  <article class="panel industry">
    <h2 class="heading heading--rule">About our industry</h2>
    <p class="lead">Pawnbroking is the oldest form of regulated consumer credit.</p>
    <ul class="icon-list">
      <li><svg><use href="#icon-ring"/></svg>The Department of Consumer and Business Services licenses pawnbrokers to do business in Oregon.</li>
      <li><svg><use href="#icon-ring"/></svg>Oregon has 68 state-licensed pawnshops, most family-owned and operated.</li>
      <li><svg><use href="#icon-ring"/></svg>Pawnbrokers offer highly regulated, safe loans to consumers on a secured basis.</li>
      <li><svg><use href="#icon-ring"/></svg>Lending is based only on collateral; pawn loans are non-recourse, with no credit reports or collections.</li>
      <li><svg><use href="#icon-ring"/></svg>Pawnbrokers provide safe, secure storage for items, including tools, equipment and jewelry.</li>
    </ul>
    <div class="photo" role="img" aria-label="Photo of two women reviewing paperwork at a desk"></div>
    <svg class="photo-arc" viewBox="0 0 373 90" preserveAspectRatio="none" aria-hidden="true">
      <path d="M0 0 Q250 90 373 40 L373 0 Z" fill="#ffffff"/>
    </svg>
  </article>

  <article class="panel regulation">
    <h2 class="heading heading--rule">Regulation</h2>
    <p class="lead">Pawnshops are heavily regulated and work closely with federal, state and local government and law enforcement.</p>
    <ul class="dot-list">
      <li>ORS 726 and OAR 441-740 set the licensing rules for the industry in Oregon.</li>
      <li>Transactions require customer ID and photo documentation.</li>
      <li>All transactions are reported daily to law enforcement.</li>
      <li>Oregon pawnbrokers work closely with these agencies:
        <ul class="sub-list dot-list">
          <li>Department of Consumer and Business Services</li>
          <li>Bureau of Alcohol, Tobacco and Firearms</li>
          <li>Oregon State Police</li>
          <li>Department of Agriculture</li>
        </ul>
      </li>
    </ul>
    <div class="about-assoc">
      <h3>About the Willamette<br>Pawnbrokers Alliance</h3>
      <p>Represents most licensed pawnbrokers statewide; members commit to a code of ethics and ongoing education.</p>
      <p>A single point of contact for Oregon regulators and lawmakers.</p>
    </div>
    <div class="photo photo--circle" role="img" aria-label="Photo of team members joining hands over a table"></div>
  </article>

  <article class="panel stats">
    <div class="photo" role="img" aria-label="Photo of a team meeting around a table in a brick-walled office"></div>
    <svg class="photo-arc" viewBox="0 0 373 90" preserveAspectRatio="none" aria-hidden="true">
      <path d="M0 90 L0 50 Q120 0 373 60 L373 90 Z" fill="#ffffff"/>
    </svg>
    <div class="content">
      <h2 class="heading heading--rule">Oregon pawnbroker statistics<small>(as reported by DCBS)</small></h2>
      <ul class="dot-list">
        <li>Average loan amount in 2020 was $170.</li>
        <li>Redemption rate of 79%.</li>
        <li>About 300,000 loans were made in 2020, totaling $51 million.</li>
        <li>Default pickup rate of 21%.</li>
      </ul>
    </div>
    <div class="quick-facts">
      <h3>Quick facts about<br>Oregon pawnbrokers</h3>
      <ul class="tick-list">
        <li><svg><use href="#icon-tick"/></svg>Licensed and bonded</li>
        <li><svg><use href="#icon-tick"/></svg>Reported daily to police</li>
        <li><svg><use href="#icon-tick"/></svg>No credit reports</li>
        <li><svg><use href="#icon-tick"/></svg>Non-recourse loans</li>
      </ul>
      <div class="url-bar">www.willamettepawnalliance.org</div>
    </div>
  </article>
</section>

</body>
</html>
```